Tri-fold Brochure Design for Banking Business

The brochure we have needs to be improved - more business like and more attractive. Logo file and brochure is attached. I would like to be able to edit the text after you get done. Your ideas and changes to text are welcome. See our website www.korvanbridgegrp.com for our theme. We can use indesign to edit the text after you complete. However, please make changes to the text we have in the design that it uploaded. Your comments and changes are welcome.

Target Market(s)

Human Resources and learning & development staff at the global investment banks - Pellham Trask, QWNR, etc.

Industry/Entity Type

Investment Banking

Logo Text

Korvan Bridge Group

Font styles to use
Serif
Sans Serif

Colors
33a6d7
0493ce
3277b5
fbf289
fdf9cf
fbee3e
0555a3
85acd3

Requirements
Must have
• Must be similar to our website www.korvanbridgegrp.com. Needs to be business-like, clean fonts, sharp design. Our logo - of course.
Nice to have
• City images - seems to be our theme.

```html
<!DOCTYPE html>
<html lang="en">
<head>
<meta charset="utf-8">
<title>Korvan Bridge Group – Tri-fold Brochure Outside</title>
<link href="https://fonts.googleapis.com/css2?family=Montserrat:wght@400;600;700&family=Questrial&display=swap" rel="stylesheet">
<style>
  :root {
    --page: #ffffff;
    --sky-top: #4fa9de;
    --sky-mid: #7cc2ec;
    --sky-low: #a9dcf3;
    --city-dark: #5a6470;
    --city-warm: #9a8572;
    --water: #4f8aa8;
    --water-deep: #35708f;
    --accent-yellow: #fbee3e;
    --marker-yellow: #fbf289;
    --marker-light: #fdf9cf;
    --marker-number: #3277b5;
    --brand-navy: #0b1e3a;
    --text-white: #ffffff;
    --map-tone: rgba(222, 240, 252, 0.55);
  }
  * { box-sizing: border-box; margin: 0; padding: 0; }
  html, body { width: 1200px; height: 1000px; overflow: hidden; background: var(--page); }
  body { position: relative; font-family: "Montserrat", Arial, sans-serif; }

  .brochure {
    position: absolute; left: 28px; top: 57px; width: 1144px; height: 885px; overflow: hidden;
  }
  .brochure__backdrop {
    position: absolute; inset: 0;
    background: linear-gradient(180deg,
      var(--sky-top) 0%, var(--sky-mid) 35%, var(--sky-low) 55%,
      #c9d6d8 60%, var(--city-dark) 70%, var(--city-warm) 80%,
      #6f7780 87%, var(--water) 89%, var(--water-deep) 100%);
  }

  .heading {
    position: absolute; top: 40px; font-family: "Questrial", Arial, sans-serif;
    color: var(--accent-yellow); font-size: 33px; letter-spacing: 1.5px; white-space: nowrap;
    transform: translateX(-50%);
  }
  .heading--about { left: 187px; }
  .heading--contact { left: 567px; }

  .about { position: absolute; left: 39px; top: 150px; width: 310px; color: var(--text-white); }
  .about p { font-size: 15.3px; line-height: 19.5px; margin-bottom: 26px; }

  .world-map {
    position: absolute; left: 378px; top: 122px; width: 380px; height: 152px;
    background: var(--map-tone); border-radius: 40% 45% 35% 50% / 50% 40% 55% 45%; opacity: .8;
  }
  .map-marker { position: absolute; width: 22px; height: 28px; }

  .contacts { position: absolute; left: 418px; top: 284px; list-style: none; }
  .contacts li { position: relative; padding-left: 48px; height: 47.5px; color: var(--text-white); }
  .contacts .marker { position: absolute; left: 0; top: 2px; width: 30px; height: 38px; }
  .contacts .region { display: block; font-weight: 700; font-size: 13px; line-height: 16px; padding-top: 4px; }
  .contacts .email { display: block; font-size: 13px; line-height: 15px; }

  .brand {
    position: absolute; left: 826px; top: 34px; display: flex; align-items: center; gap: 12px;
  }
  .brand__mark { width: 40px; height: 40px; background: var(--marker-number); }
  .brand__name {
    font-family: "Montserrat", Arial, sans-serif; font-weight: 600; font-size: 21px;
    line-height: 24px; color: var(--brand-navy); letter-spacing: 1px; text-transform: uppercase;
  }

  .tagline {
    position: absolute; left: 952px; top: 224px; transform: translateX(-50%);
    font-family: "Questrial", Arial, sans-serif; color: var(--text-white);
    font-size: 31px; line-height: 40.5px; letter-spacing: 2.5px; text-align: center; text-transform: uppercase;
  }

  .footer {
    position: absolute; left: 568px; top: 806px; transform: translateX(-50%);
    text-align: center; color: var(--text-white); white-space: nowrap;
  }
  .footer__web { font-size: 19px; line-height: 22px; }
  .footer__service { font-weight: 700; font-size: 16px; letter-spacing: .5px; line-height: 22px; }
</style>
</head>
<body>
<main class="brochure">
  <div class="brochure__backdrop" role="img" aria-label="Photograph of a city skyline across the water under a clear blue sky"></div>

  <h2 class="heading heading--about">ABOUT US</h2>
  <h2 class="heading heading--contact">GET IN TOUCH</h2>

  <section class="about">
    <p>Korvan Bridge Group efficiently provides complete sales, marketing and logistical support for all our programs, no matter the location.</p>
    <p>Our globally located trainers have extensive experience, both as industry professionals and as trainers.</p>
    <p>Our highly qualified logistical team complement the training services, providing reliable and efficient support.</p>
  </section>

  <div class="world-map" role="img" aria-label="Light world map showing office regions"></div>
  <svg class="map-marker" style="left:566px;top:188px" viewBox="0 0 22 28"><polygon points="1,1 21,1 11,27" fill="var(--marker-yellow)"/><text x="10" y="12" font-size="8" fill="var(--marker-number)" text-anchor="middle" font-family="Montserrat, sans-serif">1.</text></svg>
  <svg class="map-marker" style="left:650px;top:134px" viewBox="0 0 22 28"><polygon points="1,1 21,1 11,27" fill="var(--marker-yellow)"/><text x="10" y="12" font-size="8" fill="var(--marker-number)" text-anchor="middle" font-family="Montserrat, sans-serif">2.</text></svg>
  <svg class="map-marker" style="left:442px;top:146px" viewBox="0 0 22 28"><polygon points="1,1 21,1 11,27" fill="var(--marker-yellow)"/><text x="10" y="12" font-size="8" fill="var(--marker-number)" text-anchor="middle" font-family="Montserrat, sans-serif">3.</text></svg>
  <svg class="map-marker" style="left:560px;top:126px" viewBox="0 0 22 28"><polygon points="1,1 21,1 11,27" fill="var(--marker-yellow)"/><text x="10" y="12" font-size="8" fill="var(--marker-number)" text-anchor="middle" font-family="Montserrat, sans-serif">4.</text></svg>

  <ul class="contacts">
    <li><svg class="marker" viewBox="0 0 30 38"><polygon points="1,1 29,1 15,37" fill="var(--marker-yellow)"/><text x="14" y="15" font-size="10" fill="var(--marker-number)" text-anchor="middle" font-family="Montserrat, sans-serif">1.</text></svg><span class="region">GLOBAL:</span><span class="email">nadia.ferrow@korvanbridgegrp.com</span></li>
    <li><svg class="marker" viewBox="0 0 30 38"><polygon points="1,1 29,1 15,37" fill="var(--marker-yellow)"/><text x="14" y="15" font-size="10" fill="var(--marker-number)" text-anchor="middle" font-family="Montserrat, sans-serif">2.</text></svg><span class="region">ASIA:</span><span class="email">owen.castell@korvanbridgegrp.com</span></li>
    <li><svg class="marker" viewBox="0 0 30 38"><polygon points="1,1 29,1 15,37" fill="var(--marker-yellow)"/><text x="14" y="15" font-size="10" fill="var(--marker-number)" text-anchor="middle" font-family="Montserrat, sans-serif">3.</text></svg><span class="region">UNITED STATES:</span><span class="email">paul.renwick@korvanbridgegrp.com</span></li>
    <li><svg class="marker" viewBox="0 0 30 38"><polygon points="1,1 29,1 15,37" fill="var(--marker-yellow)"/><text x="14" y="15" font-size="10" fill="var(--marker-number)" text-anchor="middle" font-family="Montserrat, sans-serif">4.</text></svg><span class="region">EUROPE:</span><span class="email">liam.hartner@korvanbridgegrp.com</span></li>
  </ul>

  <div class="brand">
    <span class="brand__mark"></span>
    <span class="brand__name">Korvan<br>Bridge Group</span>
  </div>

  <h1 class="tagline">Your<br>Expert<br>Training<br>and<br>Consulting<br>Partner</h1>

  <footer class="footer">
    <p class="footer__web">www.korvanbridgegrp.com</p>
    <p class="footer__service">WORLDWIDE TRAINING SERVICE</p>
  </footer>
</main>
</body>
</html>
```